Corporate holiday party invitation

Please design a holiday party invitations that looks classy and festive for our member holiday party. The event is first class, semi-formal and needs to be conveyed as such. Please see file from last year so you can see what we are aiming for. The new wording for the invite is as follows: (please use similar fonts to the file provided)

BVK Dallas/Fort Worth
cordially invites you and a guest to the
Yearly Winter Guild Supper Soiree
on Thursday, December 16th
at 6:30pm in the evening

Merrow Tower, Lantern Club
4817 Pell Avenue, 40th floor
Dallas, TX 75288

Tickets are $100 per person and include:
open premium bar, appetizers, three course dinner
and entertainment

Holiday Cocktail Dress

Target Market(s)

middle aged corporate types

Industry/Entity Type

Event

Font styles to use
Script

Requirements
Must have
• Classy holiday feel and design elements,

```html
<!DOCTYPE html>
<html lang="en">
<head>
<meta charset="utf-8">
<title>BVK Dallas/Fort Worth — Yearly Winter Guild Supper Soiree Invitation</title>
<link rel="stylesheet" href="https://fonts.googleapis.com/css2?family=Tangerine:wght@400;700&family=Cormorant+Garamond:ital,wght@0,500;1,500&display=swap">
<style>
  :root {
    --charcoal: #1b1b1d;
    --charcoal-deep: #0e0e10;
    --stripe: rgba(255, 255, 255, 0.035);
    --gold-bright: #f4dc86;
    --gold: #d8b24a;
    --gold-deep: #8a6a1c;
    --gold-pale: #d9c38a;
  }
  html, body {
    margin: 0;
    padding: 0;
    overflow: hidden;
    background: var(--charcoal-deep);
  }
  .invitation {
    position: relative;
    width: 876px;
    height: 1200px;
    overflow: hidden;
    background:
      repeating-linear-gradient(90deg, transparent 0 7px, var(--stripe) 7px 8px),
      radial-gradient(ellipse at 40% 45%, #2a2a2d 0%, var(--charcoal) 55%, var(--charcoal-deep) 100%);
  }
  .corner-ornament {
    position: absolute;
    left: 0;
    top: 0;
    width: 150px;
    height: 120px;
    background: linear-gradient(135deg, var(--gold-deep) 0%, var(--gold) 40%, var(--gold-bright) 60%, transparent 62%);
  }
  .flourish-ornament {
    position: absolute;
    right: 0;
    top: 0;
    width: 300px;
    height: 1200px;
    background:
      linear-gradient(90deg, transparent 0%, rgba(216, 178, 74, 0.10) 40%, rgba(216, 178, 74, 0.32) 100%),
      linear-gradient(180deg, rgba(244, 220, 134, 0.18) 0%, transparent 50%, rgba(244, 220, 134, 0.18) 100%);
  }
  .script-line {
    position: absolute;
    margin: 0;
    font-family: "Tangerine", cursive;
    font-weight: 700;
    font-size: 66px;
    line-height: 1;
    white-space: nowrap;
    background: linear-gradient(180deg, var(--gold-bright) 0%, var(--gold) 55%, var(--gold-deep) 100%);
    -webkit-background-clip: text;
    background-clip: text;
    color: transparent;
  }
  .host { left: 110px; top: 190px; font-size: 74px; }
  .invite { left: 110px; top: 250px; font-size: 60px; }
  .event-name { left: 140px; top: 316px; font-size: 64px; }
  .event-date { left: 205px; top: 390px; font-size: 62px; }
  .event-time { left: 250px; top: 450px; font-size: 62px; }

  .details {
    position: absolute;
    left: 110px;
    width: 780px;
    margin: 0;
    text-align: center;
    font-family: "Cormorant Garamond", serif;
    font-weight: 500;
    color: var(--gold-pale);
    white-space: nowrap;
  }
  .venue {
    top: 605px;
    left: 330px;
    width: 320px;
    font-size: 36px;
    line-height: 48px;
  }
  .tickets {
    top: 770px;
    left: 0;
    width: 876px;
    padding-right: 60px;
    box-sizing: border-box;
    font-size: 36px;
    line-height: 48px;
  }
  .dress-code {
    top: 1022px;
    left: 110px;
    width: 660px;
    font-size: 38px;
  }
</style>
</head>
<body>
  <main class="invitation">
    <div class="corner-ornament" role="img" aria-label="Gold curled page corner ornament"></div>
    <div class="flourish-ornament" role="img" aria-label="Gold swirling filigree flourishes along the right edge"></div>

    <p class="script-line host">BVK Dallas/Fort Worth</p>
    <p class="script-line invite">cordially invites you and a guest to the</p>
    <p class="script-line event-name">Yearly Winter Guild Supper Soiree</p>
    <p class="script-line event-date">on Thursday, December 16th</p>
    <p class="script-line event-time">at 6:30pm in the evening</p>

    <p class="details venue">Merrow Tower, Lantern Club<br>4817 Pell Avenue, 40th floor<br>Dallas, TX 75288</p>
    <p class="details tickets">Tickets are $100 per person and include:<br>open premium bar, appetizers, three course dinner<br>and entertainment</p>
    <p class="details dress-code">Holiday Cocktail Dress</p>
  </main>
</body>
</html>
```